Letterhead to coordinate with business card

I am needing a docx template and print file for a letterhead to co-ordinate with my newly designed logo and business card.

```html
<!DOCTYPE html>
<html lang="en">
<head>
<meta charset="utf-8">
<title>Harbor Plan Services – Letterhead</title>
<link rel="stylesheet" href="https://fonts.googleapis.com/css2?family=Montserrat:ital,wght@0,400;0,600;0,700;1,400&family=Roboto+Condensed:wght@700&display=swap">
<style>
  :root {
    --canvas: #e4e4e2;
    --paper: #ffffff;
    --ink: #3a3a3c;
    --ink-soft: #4a4a4d;
    --magenta: #a8306a;
    --magenta-deep: #6b2e48;
    --teal: #0e7f7b;
    --teal-deep: #1b5d5b;
    --navy: #2f3441;
    --footer-text: #ffffff;
    --sign-area: #f1f1f2;
  }
  * { box-sizing: border-box; margin: 0; padding: 0; }
  html, body { width: 1200px; height: 1200px; overflow: hidden; }
  body {
    background: var(--canvas);
    font-family: "Montserrat", sans-serif;
    color: var(--ink);
    position: relative;
  }
  .letterhead {
    position: absolute;
    left: 160px;
    top: 30px;
    width: 881px;
    height: 1140px;
    background: var(--paper);
    overflow: hidden;
    box-shadow: 0 2px 10px rgba(0,0,0,0.08);
  }
  .footer-band {
    position: absolute;
    left: 0;
    right: 0;
    top: 900px;
    bottom: 0;
    background:
      linear-gradient(180deg, rgba(47,52,65,0) 0%, var(--navy) 70%),
      linear-gradient(90deg, var(--magenta-deep) 0%, var(--navy) 50%, var(--teal-deep) 100%);
  }
  .brand {
    position: absolute;
    left: 617px;
    top: 69px;
    width: 213px;
    display: flex;
    flex-direction: column;
    align-items: center;
    gap: 14px;
  }
  .brand-square {
    width: 82px;
    height: 82px;
    background: var(--magenta);
  }
  .brand-name {
    font-weight: 600;
    font-size: 19px;
    line-height: 1.2;
    color: var(--magenta);
    text-align: center;
  }
  .letter-date {
    position: absolute;
    left: 116px;
    top: 231px;
    font-weight: 700;
    font-size: 15px;
  }
  .recipient {
    position: absolute;
    left: 116px;
    top: 290px;
    font-size: 15px;
    line-height: 22px;
  }
  .recipient-name { font-weight: 700; }
  .recipient-role { font-style: italic; }
  .letter-body {
    position: absolute;
    left: 116px;
    top: 398px;
    width: 628px;
    font-size: 15.3px;
    line-height: 24.2px;
    color: var(--ink-soft);
  }
  .letter-body p + p { margin-top: 19px; }
  .sign-off {
    position: absolute;
    left: 612px;
    top: 748px;
    width: 180px;
    text-align: center;
    font-size: 15px;
  }
  .signature {
    width: 150px;
    height: 44px;
    margin: 8px auto 4px;
    background: var(--sign-area);
    border-radius: 4px;
  }
  .signer { font-weight: 700; }
  .contact-row {
    position: absolute;
    left: 42px;
    right: 40px;
    top: 1091px;
    display: flex;
    justify-content: space-between;
    align-items: center;
    font-family: "Roboto Condensed", sans-serif;
    font-weight: 700;
    font-size: 13px;
    color: var(--footer-text);
  }
  .contact-item { display: flex; align-items: center; gap: 7px; white-space: nowrap; }
  .contact-icon { width: 17px; height: 17px; flex: none; }
</style>
</head>
<body>
  <main class="letterhead">
    <div class="footer-band" role="img" aria-label="Decorative footer artwork in magenta and teal over a dark navy base"></div>

    <header class="brand">
      <div class="brand-square"></div>
      <div class="brand-name">Harbor Plan<br>Services</div>
    </header>

    <p class="letter-date">Date, 22 February 2022</p>

    <div class="recipient">
      <p>To:</p>
      <p class="recipient-name">Alex Carter</p>
      <p class="recipient-role">Chief Officer</p>
    </div>

    <section class="letter-body">
      <p>Lorem ipsum dolor sit amet, consectetur adipiscing elit. Duis auctor sem vel metus interdum porta. Duis consequat bibendum felis eget cursus. Nulla eget purus vehicula ipsum finibus egestas. Nullam ligula ipsum, mollis sed gravida vitae, maximus eu dolor. Morbi luctus sem a congue consectetur.</p>
      <p>Orci varius natoque penatibus et magnis dis parturient montes, nascetur ridiculus mus. Vestibulum congue eros auctor, ullamcorper libero blandit, tempor tellus. Proin vitae tellus et nunc fringilla lacinia. Sed augue erat, facilisis laoreet velit a, convallis mattis nunc. Nunc sagittis ligula vitae sollicitudin sollicitudin.</p>
      <p>Nulla facilisi. Nulla quis odio vitae purus aliquam fermentum ut nec diam. Fusce sed velit ultrices, aliquam augue ut, sollicitudin orci.</p>
    </section>

    <div class="sign-off">
      <p>Kind Regards</p>
      <div class="signature" role="img" aria-label="Handwritten signature of the sender"></div>
      <p class="signer">Alex Carter</p>
    </div>

    <footer class="contact-row">
      <span class="contact-item">
        <svg class="contact-icon" viewBox="0 0 20 20" aria-hidden="true"><circle cx="10" cy="10" r="10" fill="var(--teal)"/><rect x="7" y="4.5" width="6" height="11" rx="1.2" fill="none" stroke="#fff" stroke-width="1.4"/><circle cx="10" cy="13.4" r="0.7" fill="#fff"/></svg>
        0400 123 456
      </span>
      <span class="contact-item">
        <svg class="contact-icon" viewBox="0 0 20 20" aria-hidden="true"><circle cx="10" cy="10" r="10" fill="var(--teal)"/><rect x="5" y="6.5" width="10" height="7" fill="#fff"/><path d="M5 6.5 L10 10.5 L15 6.5" fill="none" stroke="var(--teal)" stroke-width="1"/></svg>
        hello@harborplanservices.com.au
      </span>
      <span class="contact-item">
        <svg class="contact-icon" viewBox="0 0 20 20" aria-hidden="true"><circle cx="10" cy="10" r="10" fill="var(--teal)"/><circle cx="10" cy="10" r="5" fill="none" stroke="#fff" stroke-width="1.2"/><ellipse cx="10" cy="10" rx="2.2" ry="5" fill="none" stroke="#fff" stroke-width="1"/><line x1="5" y1="10" x2="15" y2="10" stroke="#fff" stroke-width="1"/></svg>
        www.harborplanservices.com.au
      </span>
      <span class="contact-item">
        <svg class="contact-icon" viewBox="0 0 20 20" aria-hidden="true"><circle cx="10" cy="10" r="10" fill="var(--teal)"/><path d="M10 15.5 C7 12 6 10.2 6 8.5 A4 4 0 0 1 14 8.5 C14 10.2 13 12 10 15.5 Z" fill="#fff"/><circle cx="10" cy="8.5" r="1.5" fill="var(--teal)"/></svg>
        PO Box 204, Lakeview NSW 2300
      </span>
    </footer>
  </main>
</body>
</html>
```